Etikett für Honigunternehmen gesucht
Zielgruppe
Wir produzieren Honig, möchten aber in naher Zukunft auch andere Honigprodukte produzieren (Cremen, Wein, Likör......). Unsere Zielgruppe sind alle.
Aufgabenstellung
Wir wünschen uns Schlichtheit und Einfachheit. Wichtig ist uns auch, dass das Design modern wirkt. Es soll kein typisches Honigetikett mit 'Wiesen und Bienen' werden. Das Glas wird auch schlicht und modern werden. Es wird nur 250-g- und 500-g-Gläser geben. Die Gewichtsangabe muss sichtbar und mind. 4 mm groß sein. Name, Anschrift und Telefonnummer können auch am Deckel oder ganz klein und leserlich am unteren Etikettenrand stehen. Dabei ist zu beachten, dass der kleinste Buchstabe min. 1,2 mm groß ist.
Etiketten-Design für Honigglas Etiketten-Design für Honigglas"
Format: Etikett für 250-gr.-Honigglas (TO ∅ 63 mm). Standardmaßgrösse 165 × 40 mm Design: schlicht, hochwertig, modern, edel/royal, unkonventionelles Design (weg von Bienen, Waben, Landschaften usw.), dunkle Farbtöne in Kontrast zu heller Schrift, die beiden Textbausteine 'Los Nr. ' sowi..
Attraktives Etiketten-Design für Honig Attraktives Etiketten-Design für Honig"
Wir verkaufen zur Zeit vor allem Waldhonig, streben aber auch einen Blütenhonig an. Das Etikett soll daher entweder den Wald wiederspiegeln oder aber neutral sein, so dass der Schriftzug Waldhonig oder Blütenhonig jeweils eingesetzt werden kann. Wichtig ist mir der Ortszusatz 'aus dem Glottertal..
Etiketten-Design für Produkte eines Familienbetriebs mit Imkerei und Hühnerhaltung Etiketten-Design für Produkte eines Familienbetriebs mit Imkerei und Hühnerhaltung"
1. Zentrale, auf allen Etiketten wiederkehrende Elemente: - Unser Riegelhaus (stilisiert) (Bild beiliegend) - Das Wort 'Marlock' (Anmerkung: ohne Anführungszeichen) - die zentralen Elemente sollen die Produkte nicht überragen. 2. Dezente Adresse: - Familie Obrecht, Talbrunn, CH-9388 Forlenz 3...
Etiketten-Design für Kurkuma-Honig Etiketten-Design für Kurkuma-Honig"
Etikett für 500g // Stanze eckig (210x35mm), Druckdatei entsprechend Vorgaben https://etikettwerk-muster.de/faq/ Vorgaben für das Grünquell Logo im Anhang Vorgaben für EG Öko Logo : https://example-oekoamt.eu/landbau/bio/download/logo_de Pflichtangaben auf dem Etikett: Gewicht, Adresse siehe Beispiel..
Etiketten-Design für Blütenhonig und Waldhonig gesucht Etiketten-Design für Blütenhonig und Waldhonig gesucht"
Zwei verschiedene Etiketten-Desings 1 x Blütenhonig sowie 1 x Waldhonig für unterschiedliche Honigglasgrößen (500 g und 250 g) Die Maße für die Etiketten wären: Für 500-Gramm-Glas 210 mm x 45 mm für's 250-Gramm-Glas 180 mm x 38 mm. Wir sind auch offen für neue Vorschläge bezüglich ..

```html
<!DOCTYPE html>
<html lang="de">
<head>
<meta charset="utf-8">
<title>Berthold Honig – Etikett Blütenhonig</title>
<link rel="stylesheet" href="https://fonts.googleapis.com/css2?family=Comfortaa:wght@300;400&display=swap">
<style>
  :root {
    --bg: #fdedc8;
    --label: #ffffff;
    --honey: #f5a40f;
    --honey-deep: #e8900a;
    --honey-light: #fbc23a;
    --band: #e9a866;
    --ink: #f2a20c;
    --paper-text: #ffffff;
  }
  * { margin: 0; padding: 0; box-sizing: border-box; }
  html, body { width: 1200px; height: 849px; overflow: hidden; }
  body {
    background: var(--bg);
    font-family: "Comfortaa", sans-serif;
    display: flex;
    align-items: center;
    justify-content: center;
  }
  .label-sheet {
    width: 960px;
    display: flex;
    flex-direction: column;
  }
  .glass-top {
    height: 150px;
    background: linear-gradient(180deg, var(--honey-light), var(--honey));
    display: flex;
    flex-direction: column;
    align-items: center;
    justify-content: center;
    color: var(--paper-text);
  }
  .glass-top .variety { font-size: 44px; font-weight: 300; letter-spacing: 1px; }
  .glass-top .weight { font-size: 20px; margin-top: 8px; }
  .label {
    height: 250px;
    background: var(--label);
    display: flex;
  }
  .label-main {
    flex: 1;
    display: flex;
    flex-direction: column;
    justify-content: center;
    padding: 0 60px 0 90px;
  }
  .brand {
    display: flex;
    align-items: center;
    gap: 22px;
    color: var(--ink);
    font-size: 66px;
    font-weight: 300;
    letter-spacing: 2px;
  }
  .brand-dot {
    width: 44px; height: 44px;
    border-radius: 50%;
    background: var(--ink);
    flex: none;
  }
  .address {
    margin-top: 34px;
    color: var(--ink);
    font-size: 13px;
    line-height: 1.35;
    font-weight: 400;
  }
  .address span { margin-right: 18px; }
  .label-band {
    width: 96px;
    background: var(--band);
    color: var(--paper-text);
    display: flex;
    align-items: center;
    justify-content: center;
    gap: 10px;
    writing-mode: vertical-rl;
  }
  .label-band .variety { font-size: 30px; font-weight: 300; }
  .label-band .weight { font-size: 18px; }
  .bee-pattern {
    height: 150px;
    background: linear-gradient(180deg, var(--honey), var(--honey-deep));
  }
</style>
</head>
<body>
  <main class="label-sheet">
    <section class="glass-top">
      <div class="variety">Blütenhonig</div>
      <div class="weight">500g</div>
    </section>
    <section class="label">
      <div class="label-main">
        <div class="brand"><span class="brand-dot"></span>Berthold Honig</div>
        <div class="address">
          <div><span>Berthold Wenzler</span>|<span></span> Am Lindenhang 14 <span></span>|<span></span> 4283 Bad Zellhof</div>
          <div><span>Herkunftsland</span><span>Österreich</span>|<span></span> Tel: <span></span>+436605172438O</div>
        </div>
      </div>
      <div class="label-band">
        <span class="variety">Blütenhonig</span>
        <span class="weight">500g</span>
      </div>
    </section>
    <section class="bee-pattern" role="img" aria-label="Weißes Bienenmuster auf Honiggrund"></section>
  </main>
</body>
</html>
```